"Wellenhafen" private practice for physiotherapy

we are looking for a flyer design for a private practice for physiotherapy. the name of the practice is "Wellenhafen".
Treatments such as: manual therapy, manual lymphatic drainage, classic massage, sectoral alternative practitioners are offered

The flyers should be double-sided and the format DIN long (105x210 mm)

Font styles to use
Serif

Colors
0094D4
00A9DD
6FCCEA
C7EBF8
E9F6FB

Requirements
Must have
• Wellenhafen, Lindenweg 17, 04719 Sangerhausen / Wellenhafen-praxis-beispiel.de / Tel. 03471 5820317

```html
<!DOCTYPE html>
<html lang="en">
<head>
<meta charset="utf-8">
<title>Wellenhafen – Flyer</title>
<link rel="stylesheet" href="https://fonts.googleapis.com/css2?family=Montserrat:wght@500;600;700;800&display=swap">
<style>
  :root {
    --board: #474747;
    --mark: #ffffff;
    --blue-deep: #0094D4;
    --blue: #00A9DD;
    --blue-mid: #6FCCEA;
    --blue-light: #C7EBF8;
    --blue-pale: #E9F6FB;
    --ink: #333333;
    --leaf: #7ac143;
    --white: #ffffff;
  }
  * { margin: 0; padding: 0; box-sizing: border-box; }
  html, body { width: 890px; height: 1200px; overflow: hidden; }
  body {
    position: relative;
    background: var(--board);
    font-family: "Montserrat", sans-serif;
  }
  .crop-marks { position: absolute; inset: 0; }
  .flyer {
    position: absolute;
    left: 58px; top: 52px;
    width: 771px; height: 1080px;
    overflow: hidden;
  }
  .hero-photo {
    position: absolute; inset: 0;
    background: linear-gradient(160deg, #b9dbe8 0%, #a6d3e4 35%, #9ccbdd 60%, #b3dbea 100%);
  }
  .top-wave { position: absolute; left: 0; top: 0; width: 771px; height: 400px; }
  .phone {
    position: absolute;
    right: 51px; top: 38px;
    color: var(--white);
    font-size: 30px;
    font-weight: 800;
    letter-spacing: 0.2px;
    white-space: nowrap;
  }
  .phone span { font-weight: 600; }
  .brand {
    position: absolute;
    left: 50px; top: 80px;
    width: 340px;
    text-align: center;
  }
  .brand-dot {
    width: 96px; height: 96px;
    margin: 0 auto 12px;
    border-radius: 50%;
    border: 5px solid var(--leaf);
  }
  .brand-name {
    color: var(--ink);
    font-size: 40px;
    font-weight: 600;
    letter-spacing: 1px;
    text-transform: uppercase;
  }
  .headline {
    position: absolute;
    left: 52px; top: 322px;
    color: var(--white);
    font-size: 69px;
    font-weight: 800;
    line-height: 83px;
    white-space: nowrap;
  }
  .treatment-photo {
    position: absolute;
    top: 672px;
    width: 214px; height: 214px;
  }
  .treatment-photo .disc {
    position: absolute; left: 0; top: 0;
    width: 196px; height: 196px;
    border-radius: 50%;
  }
  .treatment-photo svg { position: absolute; left: 0; top: 0; }
  .photo-shoulder .disc { background: radial-gradient(circle at 60% 45%, #e8d2c3, #f2ebe6 70%); }
  .photo-foot .disc { background: radial-gradient(circle at 50% 50%, #e3bfa5, #efe4dc 75%); }
  .photo-hand .disc { background: radial-gradient(circle at 50% 55%, #edc9b0, #f6ede8 75%); }
  .treatments {
    position: absolute;
    left: 0; top: 918px;
    width: 771px; height: 100px;
    background: linear-gradient(180deg, #0c93bf 0%, var(--blue-deep) 100%);
    color: var(--white);
  }
  .treatments-title {
    position: absolute; left: 39px; top: 22px;
    font-size: 17px; font-weight: 700; line-height: 21px;
  }
  .treatment {
    position: absolute; top: 23px;
    font-size: 15.5px; font-weight: 500; line-height: 18px;
  }
  .divider { position: absolute; top: 22px; }
  .social {
    position: absolute;
    left: 355px; top: 1026px;
    display: flex; gap: 13px;
  }
  .social span {
    width: 22px; height: 22px;
    border-radius: 50%;
    border: 1.5px solid var(--ink);
  }
  .contact {
    position: absolute;
    left: 0; top: 1056px;
    width: 771px;
    text-align: center;
    color: var(--ink);
    font-size: 11px;
    font-weight: 500;
    letter-spacing: 0.2px;
  }
</style>
</head>
<body>
  <svg class="crop-marks" width="890" height="1200" viewBox="0 0 890 1200" stroke="var(--mark)" stroke-width="1">
    <line x1="70" y1="22" x2="70" y2="50"/><line x1="28" y1="62" x2="56" y2="62"/>
    <line x1="818" y1="22" x2="818" y2="50"/><line x1="831" y1="62" x2="860" y2="62"/>
    <line x1="70" y1="1134" x2="70" y2="1162"/><line x1="28" y1="1122" x2="56" y2="1122"/>
    <line x1="818" y1="1134" x2="818" y2="1162"/><line x1="831" y1="1122" x2="860" y2="1122"/>
  </svg>

  <main class="flyer">
    <div class="hero-photo" role="img" aria-label="Photo of a relaxed woman lying on a massage table receiving a shoulder massage, in light blue tones"></div>

    <svg class="top-wave" viewBox="0 0 771 400" aria-hidden="true">
      <path d="M0 160 C120 40 280 60 420 120 C560 180 680 230 771 210 L771 0 L0 0 Z" fill="var(--blue-pale)" opacity="0.35"/>
      <path d="M0 300 C140 240 300 250 440 300 C560 345 680 360 771 300 L771 220 C680 245 560 200 420 140 C280 80 120 70 0 140 Z" fill="var(--blue-pale)" opacity="0.55"/>
    </svg>

    <div class="phone"><span>Tel:</span> 03471 5820317</div>

    <div class="brand">
      <div class="brand-dot"></div>
      <div class="brand-name">Wellenhafen</div>
    </div>

    <h1 class="headline">Feel Better<br>Reduce Pain<br>&amp; Stress</h1>

    <div class="treatment-photo photo-shoulder" style="left:48px">
      <div class="disc" role="img" aria-label="Photo of hands massaging a woman's shoulder"></div>
      <svg width="214" height="214" viewBox="0 0 214 214" aria-hidden="true"><path d="M205 110 C208 165 175 200 130 206 C170 190 196 160 198 110 Z" fill="var(--blue-deep)"/></svg>
    </div>
    <div class="treatment-photo photo-foot" style="left:288px">
      <div class="disc" role="img" aria-label="Photo of a therapist massaging a foot"></div>
      <svg width="214" height="214" viewBox="0 0 214 214" aria-hidden="true"><path d="M205 110 C208 165 175 200 130 206 C170 190 196 160 198 110 Z" fill="var(--blue-deep)"/></svg>
    </div>
    <div class="treatment-photo photo-hand" style="left:528px">
      <div class="disc" role="img" aria-label="Photo of a therapist massaging a hand"></div>
      <svg width="214" height="214" viewBox="0 0 214 214" aria-hidden="true"><path d="M205 110 C208 165 175 200 130 206 C170 190 196 160 198 110 Z" fill="var(--blue-deep)"/></svg>
    </div>

    <section class="treatments">
      <div class="treatments-title">Treatments<br>offered :</div>
      <div class="treatment" style="left:196px">manual<br>therapy</div>
      <div class="treatment" style="left:315px">manual<br>lymphatic<br>drainage</div>
      <div class="treatment" style="left:452px">classic<br>massage</div>
      <div class="treatment" style="left:580px">sectoral alternative<br>practitioners are<br>offered</div>
      <svg class="divider" style="left:282px" width="12" height="60" viewBox="0 0 12 60" aria-hidden="true"><path d="M4 0 C12 20 12 40 4 60 C8 40 8 20 4 0 Z" fill="var(--leaf)"/></svg>
      <svg class="divider" style="left:419px" width="12" height="60" viewBox="0 0 12 60" aria-hidden="true"><path d="M4 0 C12 20 12 40 4 60 C8 40 8 20 4 0 Z" fill="var(--leaf)"/></svg>
      <svg class="divider" style="left:546px" width="12" height="60" viewBox="0 0 12 60" aria-hidden="true"><path d="M4 0 C12 20 12 40 4 60 C8 40 8 20 4 0 Z" fill="var(--leaf)"/></svg>
    </section>

    <div class="social" aria-hidden="true"><span></span><span></span></div>

    <p class="contact">Wellenhafen · Lindenweg 17 · 04719 Sangerhausen · Wellenhafen-praxis-beispiel.de · Tel. 03471 5820317</p>
  </main>
</body>
</html>
```